Selfpublisher sucht Buch-/E-Book-Cover
Zielgruppe
Hallo
Ich bin Selfpublisher und schreibe gerade ein Buch mit dem Themeninhalt 'Grübeln Stoppen' und dafür benötige ich ein kreatives Ebook-Cover und Taschenbuchcover.
Aufgabenstellung
Ich habe detaillierte Vorgaben in meinem Template für den Designer vorbereitet.
Ein Stockphoto für die Covererstellung befindet sich ebenfalls im Anhang.

```html
<!DOCTYPE html>
<html lang="de">
<head>
<meta charset="utf-8">
<title>Raus aus dem Gedankenstrudel – Buchcover</title>
<link rel="stylesheet" href="https://fonts.googleapis.com/css2?family=Alegreya:wght@400&family=Alegreya+Sans:wght@700&family=Playfair+Display+SC:wght@900&display=swap">
<style>
  :root {
    --wall-light: #d9d4ab;
    --wall-mid: #b9b78f;
    --wall-dark: #7f8670;
    --floor: #3b434c;
    --floor-dark: #272d34;
    --ink: #1d1a16;
    --panel: rgba(244, 240, 205, 0.55);
    --paper: #ffffff;
    --person-shirt: #3b5673;
    --person-chair: #7a4a34;
  }
  * { margin: 0; padding: 0; box-sizing: border-box; }
  html, body { width: 1200px; height: 932px; overflow: hidden; background: #ffffff; }
  .cover { position: relative; width: 1200px; height: 932px; overflow: hidden; color: var(--ink); }
  .backdrop {
    position: absolute; inset: 0;
    background:
      radial-gradient(ellipse at 62% 28%, rgba(255,252,220,0.55), transparent 55%),
      linear-gradient(180deg, var(--wall-light) 0%, var(--wall-mid) 55%, var(--wall-dark) 79%, var(--floor) 79.6%, var(--floor-dark) 100%);
  }
  .backdrop::after {
    content: ""; position: absolute; inset: 0;
    background: radial-gradient(ellipse at 55% 40%, transparent 50%, rgba(40,45,35,0.35) 100%);
  }
  .spine-guides { position: absolute; left: 0; top: 0; }

  .back-panel {
    position: absolute; left: 43px; top: 126px;
    width: 493px; height: 541px;
    background: var(--panel);
    padding: 4px 5px 0 5px;
  }
  .back-headline {
    font-family: "Alegreya Sans", sans-serif;
    font-weight: 700; font-size: 32px; line-height: 40.5px;
    text-align: center; margin-bottom: 15px;
  }
  .back-headline span { display: block; }
  .back-copy { font-family: "Alegreya", serif; font-size: 20px; line-height: 26.4px; }
  .back-copy + .back-copy { margin-top: 26px; }
  .back-copy .row { display: block; text-align: justify; text-align-last: justify; white-space: nowrap; }
  .back-copy .row.end { text-align-last: left; }

  .isbn-field { position: absolute; left: 323px; top: 755px; width: 227px; height: 134px; background: var(--paper); }

  .spine {
    position: absolute; left: 579px; top: 100px;
    width: 43px; height: 776px;
    writing-mode: vertical-rl; transform: rotate(180deg);
    white-space: nowrap;
    font-family: "Alegreya Sans", sans-serif;
    font-weight: 700; font-size: 32px; line-height: 43px;
  }
  .spine-author { color: var(--paper); margin-right: 0; margin-bottom: 36px; }
  .spine-title { color: var(--ink); }

  .cover-photo {
    position: absolute; left: 645px; top: 303px;
    width: 228px; height: 585px;
    border-radius: 90px 90px 14px 14px;
    background: linear-gradient(180deg, #6b4a33 0%, var(--person-shirt) 22%, var(--person-shirt) 52%, var(--person-chair) 56%, var(--person-chair) 78%, #59473a 100%);
    opacity: 0.9;
  }

  .front-title {
    position: absolute; right: 33px; top: 38px;
    font-family: "Playfair Display SC", serif;
    font-weight: 900; color: var(--ink);
    text-align: right; line-height: 1;
  }
  .front-title .line { display: block; }
  .title-big { font-size: 64px; letter-spacing: 1px; }
  .title-small { font-size: 36px; }
  .line-2 { margin-top: 10px; margin-right: 58px; }
  .line-3 { margin-top: 10px; }

  .front-subtitle {
    position: absolute; right: 39px; top: 320px;
    font-family: "Alegreya Sans", sans-serif;
    font-weight: 700; font-size: 31px; line-height: 37.7px;
    text-align: right;
  }
  .front-subtitle span { display: block; white-space: nowrap; }

  .front-author {
    position: absolute; right: 48px; top: 850px;
    font-family: "Alegreya Sans", sans-serif;
    font-weight: 700; font-size: 31px; color: var(--paper);
  }
</style>
</head>
<body>
<main class="cover">
  <div class="backdrop" role="img" aria-label="Betonwand in Gelbgrün mit weißen Kreidekritzeleien, darunter dunkles Kopfsteinpflaster"></div>

  <svg class="spine-guides" width="1200" height="932" viewBox="0 0 1200 932" aria-hidden="true">
    <line x1="579" y1="18" x2="579" y2="932" stroke="#1d1a16" stroke-width="1.4" stroke-dasharray="14 9"/>
    <line x1="622" y1="18" x2="622" y2="932" stroke="#1d1a16" stroke-width="1.4" stroke-dasharray="14 9"/>
  </svg>

  <section class="back-panel">
    <h2 class="back-headline"><span>Erfahrungen aus Leben und</span><span>Praxis helfen Dir Deinen Weg</span><span>zu finden.</span></h2>
    <p class="back-copy">
      <span class="row">Grübeln ist so eine Sache für sich. Wir Menschen</span>
      <span class="row">grübeln jeden Tag, die einen mehr und die anderen</span>
      <span class="row">weniger. Doch leider sind die Mehrgrübler man-</span>
      <span class="row">chmal in einer Situation, wo Gefühle, Eindrücke und</span>
      <span class="row">spezielle Ereignisse dazu führen, dass sie aus dem</span>
      <span class="row">Grübeln nicht mehr heraus kommen. Ich selbst bin</span>
      <span class="row">gelegentlicher Grübler, dabei habe schon so manches</span>
      <span class="row">nachgedacht und meine Erfahrungen gesammelt,</span>
      <span class="row end">wie man dem Grübeln positiver gegenwirken kann.</span>
    </p>
    <p class="back-copy">
      <span class="row">In diesem Buch findest Du lösungsorientierte und</span>
      <span class="row">praxisnahe Ansätze, die dir helfen sollen dein Grü-</span>
      <span class="row">beln zu verstehen und in eine andere Richtung zu</span>
      <span class="row end">lenken.</span>
    </p>
  </section>

  <div class="isbn-field"></div>

  <div class="spine">
    <span class="spine-author">Lorenz Adler</span>
    <span class="spine-title">Raus aus dem Gedankenstrudel</span>
  </div>

  <div class="cover-photo" role="img" aria-label="Junger Mann im Jeanshemd, von hinten, auf einem braunen Stuhl vor der Wand, über seinem Kopf gezeichnete Fragezeichen"></div>

  <h1 class="front-title">
    <span class="line line-1"><span class="title-big">RAUS</span> <span class="title-small">AUS DEM</span></span>
    <span class="line line-2 title-big">GEDANKEN-</span>
    <span class="line line-3 title-big">STRUDEL</span>
  </h1>

  <p class="front-subtitle">
    <span>Bewusst&nbsp;</span>
    <span>Grübeln stoppen,</span>
    <span>schlechte Gedanken</span>
    <span>loswerden und</span>
    <span>lernen das</span>
    <span>Gedankenstrudel</span>
    <span>zu kontrollieren.</span>
  </p>

  <p class="front-author">Lorenz Adler</p>
</main>
</body>
</html>
```